nutrition ebook cover

i need a cover for a ebook designed, the book is called Amber Lattice so i would like that somewhere on the cover. i would also like the word nutrition followed by my company logo that i have attached below somewhere on the cover( i have attached two logos and would like to see with both separatley), i would like this to be faded into the background if possible, perhaps in a upper or lower corner. i would also like to see options with and without the picture i have attached below. the look I'm going for is professional and clean. this is a fat loss, healthy eating booklet. the winning designer i would like to design the following pages within the book aswell no more than 10 pages, that i will provide all content for, i just need help with putting what i have on pdf in a way that looks professional and cool. this would ideally covered in the rate that is paid for the cover. i also have other booklets i need made so the winning designer will most likely get that work too at a later date for an additional fee of course.

Industry/Entity Type

Nutrition

Requirements
Nice to have
• Outside images are welcomed, happy to purchase any stock images used from a outside source

```html
<!DOCTYPE html>
<html lang="en">
<head>
<meta charset="utf-8">
<title>Amber Lattice Nutrition – Cover Options</title>
<link rel="stylesheet" href="https://fonts.googleapis.com/css2?family=Bebas+Neue&family=Oswald:wght@500&display=swap">
<style>
  :root {
    --page: #ffffff;
    --green-deep: #1f6a12;
    --green-bright: #3c9a1c;
    --title-light: #ffffff;
    --badge-ink: #4a4a4a;
    --wood-light: #d4d4d2;
    --wood-light-2: #e6e6e4;
    --concrete: #b9bfc6;
    --concrete-2: #d2d6db;
    --wood-dark: #4a3a2c;
    --wood-dark-2: #2a2119;
    --produce-red: #c9472c;
    --produce-orange: #e48a2a;
    --produce-green: #5f8c2e;
    --produce-cream: #e9d8a6;
  }
  * { box-sizing: border-box; margin: 0; padding: 0; }
  html, body { width: 1200px; height: 651px; overflow: hidden; background: var(--page); }
  .sheet { position: relative; width: 1200px; height: 651px; }

  .cover {
    position: absolute; top: 56px; width: 337px; height: 540px; overflow: hidden;
  }
  .cover--market { left: 40px; }
  .cover--pantry { left: 432px; }
  .cover--harvest { left: 824px; }

  .cover__photo { position: absolute; inset: 0; }
  .cover--market .cover__photo {
    background:
      linear-gradient(180deg, var(--wood-light-2) 0%, var(--wood-light) 36%, rgba(212,212,210,0) 48%),
      linear-gradient(135deg, var(--produce-red) 0%, var(--produce-orange) 30%, var(--produce-cream) 55%, var(--produce-green) 80%, var(--produce-red) 100%);
  }
  .cover--pantry .cover__photo {
    background:
      linear-gradient(90deg, var(--produce-green) 0%, var(--produce-red) 10%, var(--produce-cream) 22%, rgba(210,214,219,0) 38%),
      linear-gradient(180deg, var(--concrete-2), var(--concrete));
  }
  .cover--harvest .cover__photo {
    background:
      linear-gradient(180deg, rgba(0,0,0,0) 0%, rgba(0,0,0,0) 22%, rgba(42,33,25,0) 35%),
      linear-gradient(180deg, var(--produce-red) 0%, var(--produce-green) 12%, var(--produce-orange) 20%, var(--wood-dark) 34%, var(--wood-dark) 60%, var(--wood-dark-2) 100%);
  }

  .brand-badge {
    position: absolute; display: flex; align-items: center; justify-content: center;
    width: 56px; height: 56px; border-radius: 50%;
    border: 2px solid var(--badge-ink); opacity: 0.55;
    font-family: "Oswald", sans-serif; font-weight: 500; font-size: 13px;
    letter-spacing: 1px; color: var(--badge-ink);
  }
  .cover--market .brand-badge { left: 143px; top: 16px; }
  .cover--pantry .brand-badge { left: 275px; top: 8px; }
  .cover--harvest .brand-badge { left: 68px; top: 72px; border-color: var(--title-light); color: var(--title-light); }

  .title {
    position: absolute; font-family: "Bebas Neue", sans-serif; line-height: 0.9;
  }
  .title__name { display: block; font-size: 46px; color: var(--green-deep); letter-spacing: 0.5px; }
  .title__topic { display: block; font-size: 72px; color: var(--green-bright); }
  .cover--market .title { left: 44px; top: 90px; }
  .cover--pantry .title { left: 124px; top: 248px; }
  .cover--pantry .title__name { font-size: 40px; }
  .cover--pantry .title__topic { font-size: 64px; }
  .cover--harvest .title { left: 40px; top: 376px; }
  .cover--harvest .title__name { color: var(--title-light); font-size: 48px; }
  .cover--harvest .title__topic { font-size: 76px; }
</style>
</head>
<body>
<main class="sheet">
  <section class="cover cover--market">
    <div class="cover__photo" role="img" aria-label="Fresh fruit, vegetables, salmon and dairy spread on light grey wooden boards"></div>
    <div class="brand-badge">VERDA</div>
    <h1 class="title"><span class="title__name">Amber Lattice</span><span class="title__topic">Nutrition</span></h1>
  </section>

  <section class="cover cover--pantry">
    <div class="cover__photo" role="img" aria-label="Basil, tomatoes, pasta, cheese, olives and beans along the left edge of a grey stone surface"></div>
    <div class="brand-badge">VERDA</div>
    <h1 class="title"><span class="title__name">Amber Lattice</span><span class="title__topic">Nutrition</span></h1>
  </section>

  <section class="cover cover--harvest">
    <div class="cover__photo" role="img" aria-label="Colourful vegetables and a small chalkboard on a dark rustic wooden table"></div>
    <div class="brand-badge">VERDA</div>
    <h1 class="title"><span class="title__name">Amber Lattice</span><span class="title__topic">Nutrition</span></h1>
  </section>
</main>
</body>
</html>
```